Building company requiring web site design

We need a web design for a new company based in Sydney called Harbin Building Co. We build and renovate new and existing homes for consumers. We would like to see design that use the colours red and grey. The final design should communicate innovative building but with old fashion quality, great customer service and attention to detail. I have already had a logo and stationary design completed and would like to use the these colour schemes
Updates

Target Market(s)

Home owners, investors

Industry/Entity Type

Building

Coding

Coded - Design and coding required

Number of Pages Required

5+ page

Requirements
Must have
• Home page, contact page, about us page, gallery page and testimonial page
Nice to have
• Contact form

```html
<!DOCTYPE html>
<html lang="en">
<head>
<meta charset="utf-8">
<title>Harbin Building Co</title>
<link href="https://fonts.googleapis.com/css2?family=Open+Sans:wght@400;600;700&family=Ubuntu:wght@400;500&display=swap" rel="stylesheet">
<style>
:root{
  --red:#d42b20;
  --red-deep:#a8211a;
  --ink:#222222;
  --text:#555555;
  --muted:#777777;
  --light:#f5f5f5;
  --footer:#262626;
  --footer-text:#9a9a9a;
  --white:#ffffff;
}
*{margin:0;padding:0;box-sizing:border-box}
html,body{width:1200px;height:2163px;overflow:hidden}
body{position:relative;font-family:"Open Sans",sans-serif;color:var(--text);background:var(--white)}
.abs{position:absolute}
.topbar{left:0;top:0;width:1200px;height:37px;background:var(--red);color:var(--white);font-size:12px}
.topbar .item{position:absolute;top:11px;display:flex;align-items:center;gap:8px}
.topbar .social{position:absolute;right:107px;top:9px;display:flex;gap:4px}
.topbar .social span{width:17px;height:17px;border-radius:50%;background:rgba(255,255,255,.85)}
.header{left:0;top:37px;width:1200px;height:101px;background:var(--white);box-shadow:0 2px 3px rgba(0,0,0,.25);z-index:2}
.brand{position:absolute;left:100px;top:36px;display:flex;align-items:center;gap:10px;font-family:"Ubuntu",sans-serif;font-weight:500;font-size:22px;color:var(--ink)}
.brand i{width:22px;height:22px;background:var(--red)}
.nav a{position:absolute;top:43px;transform:translateX(-50%);font-size:12px;color:var(--ink);text-decoration:none;letter-spacing:.3px}
.nav a.active{color:var(--red)}
.hero{left:0;top:138px;width:1200px;height:520px;background:linear-gradient(180deg,#a79c8c 0%,#c8bfb2 35%,#9d948a 70%,#7a736c 100%)}
.hero h1{position:absolute;left:97px;top:340px;font-size:55px;font-weight:700;color:var(--white);letter-spacing:.5px;text-shadow:0 2px 4px rgba(0,0,0,.4)}
.hero h2{position:absolute;left:97px;top:412px;font-size:29px;font-weight:400;color:var(--white);text-shadow:0 2px 4px rgba(0,0,0,.4)}
.chev{position:absolute}
.section-title{position:absolute;left:0;width:1200px;text-align:center;font-family:"Ubuntu",sans-serif;font-size:26px;color:var(--ink)}
.section-title em{font-style:normal;color:var(--red)}
.rule{position:absolute;left:565px;width:70px;height:2px;background:var(--ink)}
.lead{position:absolute;left:0;width:1200px;text-align:center;font-size:11.5px;line-height:24px;color:var(--muted)}
.services{left:0;top:890px;width:1200px;height:446px;background:linear-gradient(135deg,#c9453c 0%,#b8302a 50%,#a8251f 100%)}
.services .section-title,.services .lead{color:var(--white)}
.services .rule{background:var(--white)}
.svc{position:absolute;top:161px;width:220px;margin-left:-110px;text-align:center;color:var(--white)}
.svc .box{width:125px;height:125px;margin:0 auto;background:var(--ink);display:flex;align-items:center;justify-content:center;box-shadow:0 3px 6px rgba(0,0,0,.35)}
.svc .box.on{background:var(--red)}
.svc h3{margin-top:17px;font-weight:400;font-size:15px}
.svc p{margin-top:10px;font-size:11px;line-height:22px}
.work{position:absolute;top:1494px;width:225px;height:156px;background:linear-gradient(160deg,#c9b8a4,#8d7e6f);box-shadow:0 8px 6px -6px rgba(0,0,0,.35)}
.testimonial{left:0;top:1695px;width:1200px;height:189px;background:var(--light)}
.avatar{position:absolute;left:113px;top:26px;width:118px;height:118px;border-radius:50%;background:linear-gradient(160deg,#d9dde3,#a9b2bd);border:3px solid var(--white)}
.quote{position:absolute;left:283px;top:40px;width:790px;font-size:11px;line-height:24.5px;color:var(--muted)}
.qmark{position:absolute;font-family:Georgia,serif;font-size:34px;color:#cccccc}
.who{position:absolute;left:283px;top:129px;font-size:10.5px;color:#2a8ab8;letter-spacing:.3px}
.role{position:absolute;left:283px;top:148px;font-size:11.5px;color:var(--ink)}
.footer{left:0;top:1884px;width:1200px;height:279px;background:var(--footer);color:var(--footer-text)}
.footer h4{position:absolute;top:28px;font-weight:400;font-size:17px;color:var(--white)}
.footer .small{position:absolute;font-size:11.5px;line-height:19px}
.signup{position:absolute;left:98px;top:118px;width:264px;height:39px;display:flex}
.signup .field{flex:1;background:#151515;font-size:10.5px;color:#666;padding:13px 12px}
.signup .btn{width:79px;background:var(--red);color:var(--white);font-weight:700;font-size:12.5px;display:flex;align-items:center;justify-content:center}
.line{position:absolute;display:flex;align-items:center;gap:14px;font-size:12.5px}
.footer-brand{position:absolute;left:906px;top:66px;width:193px;text-align:center;font-family:"Ubuntu",sans-serif;font-weight:500;font-size:26px;color:#4a4a4a}
.copy{position:absolute;left:0;top:2126px;width:1200px;text-align:center;font-size:11.5px;color:var(--white)}
</style>
</head>
<body>

<div class="abs topbar">
  <div class="item" style="left:103px">
    <svg width="10" height="10" viewBox="0 0 24 24"><path fill="#fff" d="M6.6 10.8a15 15 0 006.6 6.6l2.2-2.2c.3-.3.7-.4 1-.2 1.1.4 2.3.6 3.6.6.6 0 1 .4 1 1V20c0 .6-.4 1-1 1A17 17 0 013 4c0-.6.4-1 1-1h3.5c.6 0 1 .4 1 1 0 1.3.2 2.5.6 3.6.1.3 0 .7-.2 1z"/></svg>
    <span>+61 2 5550 0148</span>
  </div>
  <div class="item" style="left:239px">
    <svg width="12" height="9" viewBox="0 0 24 18"><path fill="#fff" d="M0 0h24v18H0z"/><path fill="none" stroke="#d42b20" stroke-width="2" d="M1 1l11 9 11-9"/></svg>
    <span>harbinbuildco.com</span>
  </div>
  <div class="social"><span></span><span></span><span></span><span></span></div>
</div>

<header class="abs header">
  <div class="brand"><i></i>Harbin Building Co</div>
  <nav class="nav">
    <a class="active" style="left:541px">HOME</a>
    <a style="left:648px">ABOUT US</a>
    <a style="left:762px">SERVICES</a>
    <a style="left:874px">GALLERY</a>
    <a style="left:995px">CONTACT US</a>
    <svg class="abs" style="left:1085px;top:44px" width="13" height="13" viewBox="0 0 24 24"><circle cx="10" cy="10" r="7" fill="none" stroke="#d42b20" stroke-width="3"/><path d="M15 15l7 7" stroke="#d42b20" stroke-width="3"/></svg>
  </nav>
</header>

<section class="abs hero" role="img" aria-label="Photo of an interior room under renovation with bare plaster walls and a window">
  <h1>HARBIN BUILDING</h1>
  <h2>ON THE OTHER HAND, WE DENOUNCE</h2>
  <svg class="chev" style="left:26px;top:244px" width="20" height="32" viewBox="0 0 20 32"><path d="M17 2L3 16l14 14" fill="none" stroke="rgba(255,255,255,.8)" stroke-width="3"/></svg>
  <svg class="chev" style="left:1155px;top:244px" width="20" height="32" viewBox="0 0 20 32"><path d="M3 2l14 14L3 30" fill="none" stroke="rgba(255,255,255,.8)" stroke-width="3"/></svg>
</section>

<h2 class="section-title" style="top:697px">Welcome To <em>Harbin Building</em></h2>
<div class="rule" style="top:748px"></div>
<p class="lead" style="top:762px">Lorem Ipsum es simplemente el texto de relleno de las imprentas y archivos de texto. Lorem Ipsum ha sido el texto de relleno estándar de las industrias desde el año 1500, cuando<br>un impresor (N. del T. persona que se dedica a la imprenta) desconocido usó una galería de textos y los mezcló de tal manera que logró hacer un libro de textos especimen.<br>No sólo sobrevivió 500 años, sino que tambien ingresó como texto</p>

<section class="abs services" aria-label="Our Services">
  <h2 class="section-title" style="top:22px">Our Services</h2>
  <div class="rule" style="top:71px"></div>
  <p class="lead" style="top:95px">Sed ut perspiciatis unde omnis iste natus error sit voluptatem accusantium doloremque laudantium, totam rem aperiam, eaque ipsa quae ab illo inventore veritatis</p>

  <div class="svc" style="left:202px">
    <div class="box on"><svg width="46" height="40" viewBox="0 0 46 40"><path fill="#fff" d="M23 2L2 20h6v18h11V27h8v11h11V20h6z"/></svg></div>
    <h3>Property</h3>
    <p>At vero eos et accusamus et iusto odio<br>dignissimos ducimus qui blanditiis<br>praesentium voluptatum<br>deleniticorrupti quos</p>
  </div>
  <div class="svc" style="left:467px">
    <div class="box"><svg width="46" height="36" viewBox="0 0 46 36"><path d="M2 2v32h42" fill="none" stroke="#fff" stroke-width="2"/><rect x="9" y="18" width="5" height="12" fill="#fff"/><rect x="17" y="12" width="5" height="18" fill="#fff"/><rect x="25" y="16" width="5" height="14" fill="#fff"/><rect x="33" y="8" width="5" height="22" fill="#fff"/></svg></div>
    <h3>Development</h3>
    <p>At vero eos et accusamus et iusto odio<br>dignissimos ducimus qui blanditiis<br>praesentium voluptatum<br>deleniticorrupti quos</p>
  </div>
  <div class="svc" style="left:734px">
    <div class="box"><svg width="46" height="46" viewBox="0 0 46 46"><rect x="14" y="4" width="28" height="22" fill="none" stroke="#fff" stroke-width="2.5"/><path d="M28 26v16M20 42h16M6 18h10v10H6zM8 28v14M14 28v14" stroke="#fff" stroke-width="2.5" fill="none"/></svg></div>
    <h3>Construction</h3>
    <p>At vero eos et accusamus et iusto odio<br>dignissimos ducimus qui blanditiis<br>praesentium voluptatum<br>deleniticorrupti quos</p>
  </div>
  <div class="svc" style="left:999px">
    <div class="box"><svg width="48" height="44" viewBox="0 0 48 44"><circle cx="18" cy="24" r="10" fill="none" stroke="#fff" stroke-width="7" stroke-dasharray="5 3"/><circle cx="18" cy="24" r="4" fill="#fff"/><circle cx="37" cy="12" r="6" fill="none" stroke="#fff" stroke-width="5" stroke-dasharray="3 2"/><circle cx="37" cy="33" r="6" fill="none" stroke="#fff" stroke-width="5" stroke-dasharray="3 2"/></svg></div>
    <h3>Projects</h3>
    <p>At vero eos et accusamus et iusto odio<br>dignissimos ducimus qui blanditiis<br>praesentium voluptatum<br>deleniticorrupti quos</p>
  </div>
</section>

<h2 class="section-title" style="top:1368px">Our <em>Works</em></h2>
<div class="rule" style="top:1415px"></div>
<p class="lead" style="top:1437px;font-size:12px">At vero eos et accusamus et iusto odio dignissimos ducimus qui blanditiis praesentium voluptatum deleniti atque corrupti quos dolores et quas molestias excepturi sint</p>
<svg class="chev" style="left:42px;top:1556px" width="14" height="34" viewBox="0 0 14 34"><path d="M12 2L2 17l10 15" fill="none" stroke="#dddddd" stroke-width="2"/></svg>
<svg class="chev" style="left:1144px;top:1556px" width="14" height="34" viewBox="0 0 14 34"><path d="M2 2l10 15L2 32" fill="none" stroke="#dddddd" stroke-width="2"/></svg>
<div class="work" style="left:102px" role="img" aria-label="Photo of a house interior stripped to timber framing"></div>
<div class="work" style="left:359px;background:linear-gradient(160deg,#e9e4de,#c99a86)" role="img" aria-label="Photo of hands reviewing building plans on a table"></div>
<div class="work" style="left:617px;background:linear-gradient(160deg,#a3b1c0,#d9dde2)" role="img" aria-label="Photo of a builder at work on a site"></div>
<div class="work" style="left:875px;background:linear-gradient(160deg,#e6e1da,#b7a895)" role="img" aria-label="Photo of a newly finished kitchen interior"></div>

<section class="abs testimonial" aria-label="Testimonial">
  <div class="avatar" role="img" aria-label="Portrait photo of the client"></div>
  <span class="qmark" style="left:258px;top:16px">&ldquo;</span>
  <p class="quote">Lorem Ipsum es simplemente el texto de relleno de las imprentas y archivos de texto. Lorem Ipsum ha sido el texto de relleno estándar de las industrias desde el año 1500, cuando un impresor (N. del T. persona que se dedica a la imprenta) desconocido usó una galería On the other hand, we denounce &nbsp;moment, so blinded by desire, that they cannot foresee...</p>
  <span class="qmark" style="left:1048px;top:76px">&rdquo;</span>
  <span class="who">MARCUS HALE</span>
  <span class="role">Marketing Executive</span>
</section>

<footer class="abs footer">
  <h4 style="left:98px">NEWSLETTER</h4>
  <p class="small" style="left:98px;top:64px;width:270px">On the other hand, we denounce with righteous indignation and dislike demoralized</p>
  <div class="signup"><div class="field">Enter your email address</div><div class="btn">SIGN UP</div></div>

  <h4 style="left:424px">CONTACT US</h4>
  <p class="small" style="left:424px;top:64px;width:250px;font-size:12px">On the other hand, we denounce with righteous indignatio</p>
  <div class="line" style="left:426px;top:116px">
    <svg width="16" height="16" viewBox="0 0 24 24"><path fill="none" stroke="#9a9a9a" stroke-width="1.6" d="M6.6 10.8a15 15 0 006.6 6.6l2.2-2.2c.3-.3.7-.4 1-.2 1.1.4 2.3.6 3.6.6.6 0 1 .4 1 1V20c0 .6-.4 1-1 1A17 17 0 013 4c0-.6.4-1 1-1h3.5c.6 0 1 .4 1 1 0 1.3.2 2.5.6 3.6.1.3 0 .7-.2 1z"/></svg>
    <span>02 5550 0148</span>
  </div>
  <div class="line" style="left:426px;top:143px">
    <svg width="17" height="12" viewBox="0 0 24 17"><rect x="1" y="1" width="22" height="15" fill="none" stroke="#9a9a9a" stroke-width="1.6"/><path d="M1 1l11 8 11-8" fill="none" stroke="#9a9a9a" stroke-width="1.6"/></svg>
    <span>info@harbinbuildco.com</span>
  </div>

  <h4 style="left:718px;top:22px">SOCIAL</h4>
  <div class="line" style="left:718px;top:59px;font-size:11.5px"><svg width="8" height="8"><circle cx="4" cy="4" r="3.5" fill="#9a9a9a"/></svg><span>Socialbook</span></div>
  <div class="line" style="left:718px;top:88px;font-size:11.5px"><svg width="8" height="8"><circle cx="4" cy="4" r="3.5" fill="#9a9a9a"/></svg><span>Chirper</span></div>
  <div class="line" style="left:718px;top:116px;font-size:11.5px"><svg width="8" height="8"><circle cx="4" cy="4" r="3.5" fill="#9a9a9a"/></svg><span>Circles Plus</span></div>
  <div class="line" style="left:718px;top:145px;font-size:11.5px"><svg width="8" height="8"><circle cx="4" cy="4" r="3.5" fill="#9a9a9a"/></svg><span>Vidstream</span></div>

  <div class="footer-brand">Harbin<br>Building Co</div>
</footer>
<p class="copy">Copy right © 2016 Harbin Building. All Rights Reserved</p>

</body>
</html>
```